We would like to create a flyer with our logo I have attached and would like you to add the NorthBrambleBID logo at the bottom.
I would like the flyer to have a urban vintage style to it.
Please add:
Email: Info@northbramblebid.co.uk
Twitter account: @Northbramblebid
Facebook account: The Copperline Vintage and Antique Market
Address: The Copperline, North Bramble, Q47 2XZ
Dates: Saturday 27 september 2014
Saturday 25 October 2014
Saturday 29 November 2014.
Please hight light the dates and the location.

Target Market(s)

Every one.

Font styles to use
Other font styles liked:
• Market Deco

Requirements
Must have
• My project should be eye catching.
• Dates and location should be clear.
• Please use this font: ‘Market Deco’
• Please source images which will suit the logo and style of layout.
Nice to have
• Colours which will contrast with the logo.
• Colour of logo is: purple is P95 -16c
• The layout on the word doc I like.

```html
<!DOCTYPE html>
<html lang="en">
<head>
<meta charset="utf-8">
<title>Copperline Vintage &amp; Antique Market – Flyer</title>
<link rel="stylesheet" href="https://fonts.googleapis.com/css2?family=Arvo:wght@700&family=Oswald:wght@500&family=Alegreya+SC:wght@500&display=swap">
<style>
  :root {
    --page-bg: #e9e5e0;
    --plum: #652a57;
    --plum-light: #7a3a69;
    --plum-deep: #4e1d43;
    --navy-plum: #3b2150;
    --gold: #f1c30f;
    --gold-dark: #c99a06;
    --ink: #3a3340;
    --cream: #f4eff2;
    --ornament: #d9c6d3;
  }
  * { box-sizing: border-box; margin: 0; padding: 0; }
  html, body { width: 1200px; height: 900px; overflow: hidden; }
  body { background: var(--page-bg); position: relative; }

  .flyer {
    position: absolute; left: 295px; top: 20px; width: 610px; height: 860px;
    background: radial-gradient(ellipse at 55% 35%, var(--plum-light) 0%, var(--plum) 55%, var(--plum-deep) 100%);
    box-shadow: 0 6px 18px rgba(0,0,0,.25);
    color: var(--cream);
  }
  .frame { position: absolute; inset: 22px; border: 2px solid var(--cream); opacity: .85; }
  .corner {
    position: absolute; width: 46px; height: 46px; background: var(--ornament); opacity: .35; border-radius: 4px;
  }
  .corner--tl { left: 12px; top: 12px; }
  .corner--tr { right: 12px; top: 12px; }
  .corner--bl { left: 12px; bottom: 12px; }
  .corner--br { right: 12px; bottom: 12px; }

  .market-title {
    position: absolute; left: 50%; top: 60px; transform: translateX(-50%);
    display: flex; align-items: center; white-space: nowrap;
    font-family: "Oswald", sans-serif; font-size: 22px; letter-spacing: 1.5px; text-transform: uppercase;
  }
  .market-title__part { background: var(--navy-plum); padding: 2px 12px; border: 1px solid var(--ornament); }
  .market-title__amp {
    font-family: "Arvo", serif; color: var(--gold); font-size: 40px; margin: -14px 6px 0; line-height: 1;
  }

  .flourish-top {
    position: absolute; left: 205px; top: 120px; width: 200px; height: 56px;
    background: var(--ornament); opacity: .55; border-radius: 30px;
  }
  .flourish-side {
    position: absolute; width: 70px; height: 180px; background: var(--ornament); opacity: .45; border-radius: 35px;
  }
  .flourish-side--left { left: 58px; top: 470px; }
  .flourish-side--right { right: 58px; top: 392px; }

  .address {
    position: absolute; left: 0; right: 0; top: 198px; text-align: center;
    font-family: "Arvo", serif; font-size: 27px; line-height: 1.3; color: var(--cream);
  }

  .ribbon { position: absolute; left: 25px; top: 280px; width: 560px; height: 90px; }
  .ribbon svg { position: absolute; inset: 0; }
  .ribbon__text {
    position: absolute; left: 0; right: 0; top: 20px; text-align: center;
    font-family: "Oswald", sans-serif; font-size: 34px; letter-spacing: 4px; color: var(--ink); text-transform: uppercase;
  }

  .dates { position: absolute; left: 0; right: 0; top: 378px; text-align: center; }
  .dates__item {
    font-family: "Alegreya SC", serif; font-size: 42px; letter-spacing: 2px; color: var(--cream); line-height: 54px;
  }
  .dates__divider { display: block; margin: 10px auto; width: 340px; height: 3px; background: var(--gold); }

  .contacts {
    position: absolute; right: 50px; top: 610px; list-style: none;
    display: flex; flex-direction: column; align-items: flex-end; gap: 14px;
  }
  .contacts__row { display: flex; align-items: center; gap: 12px; }
  .contacts__icon { width: 28px; height: 28px; border-radius: 50%; background: var(--cream); display: grid; place-items: center; }
  .contacts__label {
    background: var(--navy-plum); border: 1px solid var(--ornament); padding: 2px 10px;
    font-family: "Oswald", sans-serif; font-size: 14px; letter-spacing: 1px; text-transform: uppercase;
  }

  .client-logo { position: absolute; left: 85px; top: 705px; display: flex; flex-direction: column; gap: 4px; }
  .client-logo__mark { width: 40px; height: 40px; background: var(--cream); }
  .client-logo__name { font-family: "Arvo", serif; font-size: 30px; color: var(--cream); line-height: 1.1; }
  .client-logo__tagline { font-family: "Oswald", sans-serif; font-size: 14px; color: var(--ornament); letter-spacing: .5px; }
</style>
</head>
<body>
  <main class="flyer">
    <div class="frame"></div>
    <div class="corner corner--tl" role="img" aria-label="Corner filigree ornament"></div>
    <div class="corner corner--tr" role="img" aria-label="Corner filigree ornament"></div>
    <div class="corner corner--bl" role="img" aria-label="Corner filigree ornament"></div>
    <div class="corner corner--br" role="img" aria-label="Corner filigree ornament"></div>

    <h1 class="market-title">
      <span class="market-title__part">Copperline Vintage</span>
      <span class="market-title__amp">&amp;</span>
      <span class="market-title__part">Antique Market</span>
    </h1>

    <div class="flourish-top" role="img" aria-label="Vintage scroll flourish"></div>

    <p class="address">The Copperline,<br>North Bramble, Q47 2XZ</p>

    <div class="ribbon">
      <svg viewBox="0 0 560 90" width="560" height="90" aria-hidden="true">
        <polygon points="0,40 70,40 70,88 0,88 22,64" fill="var(--gold-dark)"/>
        <polygon points="560,30 490,30 490,78 560,78 538,54" fill="var(--gold-dark)"/>
        <polygon points="45,12 515,2 515,64 45,74" fill="var(--gold)"/>
      </svg>
      <div class="ribbon__text">Every Saturday 2014</div>
    </div>

    <section class="dates">
      <p class="dates__item">27 September</p>
      <span class="dates__divider" aria-hidden="true"></span>
      <p class="dates__item">25 October</p>
      <span class="dates__divider" aria-hidden="true"></span>
      <p class="dates__item">29 November</p>
    </section>

    <div class="flourish-side flourish-side--left" role="img" aria-label="Vertical scroll flourish"></div>
    <div class="flourish-side flourish-side--right" role="img" aria-label="Vertical scroll flourish"></div>

    <ul class="contacts">
      <li class="contacts__row"><span class="contacts__icon"></span><span class="contacts__label">@Northbramblebid</span></li>
      <li class="contacts__row">
        <span class="contacts__icon">
          <svg width="16" height="12" viewBox="0 0 16 12" aria-hidden="true"><rect x="1" y="1" width="14" height="10" fill="none" stroke="var(--plum)" stroke-width="1.5"/><polyline points="1,1 8,7 15,1" fill="none" stroke="var(--plum)" stroke-width="1.5"/></svg>
        </span>
        <span class="contacts__label">Info@northbramblebid.co.uk</span>
      </li>
      <li class="contacts__row"><span class="contacts__icon"></span><span class="contacts__label">The Copperline Vintage and Antique Market</span></li>
    </ul>

    <div class="client-logo">
      <span class="client-logo__mark"></span>
      <span class="client-logo__name">northbramblebid</span>
      <span class="client-logo__tagline">Creating a Better Bramble</span>
    </div>
  </main>
</body>
</html>
```